Modern Business Card For A Digital Advertising Company

I'll be print on the Tarn Prints Velour paper http://us.tarnprints.example/products/velour/business-cards.html
Need's to be modern and use the color palette of the logo or gray scales. I think integrating the pixelation of the logo in to the card and having it wrap from one side to the other could be interesting. My company provides ad operations, web development, and number of other services to websites around the world. You can see my website at http://www.pixelharbor.example
Contact info on the card needs to have
Dana Welloby
President
p.555.318.4406
dana@pixelharbor.example
http://www.pixelharbor.example
Doesn't necessarily need to be in that order
Target Market(s)
Website owners
Industry/Entity Type
Business
Look and feel

```html
<!DOCTYPE html>
<html lang="en">
<head>
<meta charset="utf-8">
<title>Pixel Harbor — Business Card Back</title>
<link rel="stylesheet" href="https://fonts.googleapis.com/css2?family=Open+Sans:wght@700&display=swap">
<style>
  :root {
    --card-green: #628c2e;
    --card-green-light: #729b40;
    --brand-green: #8dc63f;
    --url-green: #c9ef8f;
  }
  html, body {
    margin: 0;
    padding: 0;
    width: 1200px;
    height: 733px;
    overflow: hidden;
  }
  .card-back {
    position: relative;
    width: 1200px;
    height: 733px;
    background: var(--card-green-light);
    font-family: "Open Sans", Verdana, sans-serif;
    overflow: hidden;
  }
  .backdrop {
    position: absolute;
    inset: 0;
    width: 1200px;
    height: 733px;
  }
  .backdrop .panel { fill: var(--card-green); }
  .brand-lockup {
    position: absolute;
    left: 0;
    right: 0;
    top: 280px;
    display: flex;
    justify-content: center;
    align-items: center;
    gap: 22px;
  }
  .brand-square {
    width: 58px;
    height: 58px;
    background: var(--brand-green);
  }
  .brand-name {
    margin: 0;
    font-size: 86px;
    font-weight: 700;
    line-height: 1;
    color: var(--brand-green);
    letter-spacing: -1px;
  }
  .website {
    position: absolute;
    left: 0;
    right: 0;
    top: 590px;
    margin: 0;
    text-align: center;
    font-size: 40px;
    font-weight: 700;
    line-height: 1.2;
    color: var(--url-green);
    letter-spacing: 0.5px;
  }
</style>
</head>
<body>
  <main class="card-back">
    <svg class="backdrop" viewBox="0 0 1200 733" aria-hidden="true">
      <polygon class="panel" points="300,0 1075,80 970,430 1200,500 1200,420 1200,733 1200,560 180,360" />
      <polygon class="panel" points="0,540 1200,733 0,733" />
      <polygon class="panel" points="0,0 300,0 0,120" />
      <polygon class="panel" points="830,0 1200,0 1200,60" />
    </svg>
    <div class="brand-lockup">
      <span class="brand-square" aria-hidden="true"></span>
      <h1 class="brand-name">Pixel Harbor</h1>
    </div>
    <p class="website">www.pixelharbor.example</p>
  </main>
</body>
</html>
```